Mockup design for a fashion contest website

The website is a landing page for a fashion contest. Participants are fashion students, designers, merchandisers, stylists, and other fashion enthusiasts. Website should have a clean, modern look and should be "headline-y" in nature. Website should be very visual with good use of images since the audience is fashion (specifically women's clothing). Contestants will earn points by identifying fashion/clothing items within images.

Here's what I am thinking:

Title:
Fashion Contest by Vendrow

Headlines (each with subheadline of 10-15 words )
Can you find the features in the image?
This will be a carousel showing 3-4 images with callouts
Have callouts for each of the categories like this: https://img.qorvexa.example/v/7TmWq2LpZr/fullview.jpg
Broad categories for items are labeled like:
Top
Dress
Jeans
Pants
Shorts
Blouse
Skirt
Standard
Crop Top
Shirt
Sweater
Detail fashion attributes are in the spreadsheet attached

Earn Points
and see where you stand -- leaderboard graphic
Win Prizes
Need a way to show multiple prizes here:
Grand prizes: Tablo Max, Kelvar Snapline KZ-TR720Q Wi-Fi Digital Camera, Halden QM480TXV Sewing Machine, Drevo Linemark Plus Drawing tablet
Other prizes: Noral Earlets, Gift cards to great stores: Vimo, Keto, Lumirel, etc.

What You Need To Know
How to Enter (25-30 words)
How do I qualify? (10-15 words)
What are the contest dates (10-15 words)
What is this for? (10-15 words)

----

Tell Your Friends (10 words) [Needs to be shown more prominently as we will have referral bonuses]

The Legal Stuff / Terms & Conditions
[Each subsection 50 words]
Eligibility
Winners & Prizes
Privacy Policy
Judging
Disclaimer

Other sections (shown as links on top perhaps)
Blog - standard blog format. No need for design
Forum - use threadhall software. No need for design
Standings
FAQ
Contact - link to email - no need for design

Need to have clear CTA to sign up on bottom.

Need to Design ‘Standings’ Page:

Show Leaderboard
Ranking, Username, total points, change in ranking (up or down)

Show Total number of images processed. This can be progress bar like in crowdfunding sites:
https://snapdrop.example/kWtrb/91ab3d6f27.png
It would say:
300,000 images processed by 1,000 participants
x% of 1,000,000 goal a month left

Goals and Stretch Goals for the Contest

500,000 images
Grand prizes (1 winner)
Other prizes (3 winners)

1,000,000 images
Grand prizes (2 winners)
Other prizes (6 winners)

2,000,000 images
Grand prizes (3 winners)
Other prizes (9 winners)

3,000,000 images
Grand prizes (4 winners)
Other prizes (12 winners)

How to Earn Points

Points awarded for correctly completing task
Points are deducted for making mistakes and unnecessary skips

Help
just a click away. Post a message on the community forum and ask a question.
----
High contrasty (black & white) with one color perhaps blue should be color palette. Look at our logo for design motif ideas.

Welcome to the contest. I will be guaranteeing the project once at least one usable design comes in. Good luck to all! Added Tuesday, March 14, 2017

Target Market(s)

Fashion community

Industry/Entity Type

Fashion

Number of Pages Required

2 page

Font styles to use
Sans Serif

Requirements
Must have
• one page scroll website (the quiz is a separate page though)
• beautiful graphics and images
• placeholder text where number of words is written
Nice to have
• written copy ideas
Should not have
• the vendrow logo should not be prominently featured. the emphasis is on 'Fashion Contest'

```html
<!DOCTYPE html>
<html lang="en">
<head>
<meta charset="utf-8">
<title>Fashion Contest by Vendrow</title>
<link rel="stylesheet" href="https://fonts.googleapis.com/css2?family=Raleway:wght@400;500;600;700;800&display=swap">
<style>
:root{
  --blue:#1e8fdc;
  --blue-soft:#e4f1fb;
  --ink:#1c1c1c;
  --text:#444;
  --muted:#8a8a8a;
  --line:#e3e3e3;
  --panel:#f3f3f3;
  --dark:#1d1d1f;
  --white:#fff;
}
*{box-sizing:border-box;margin:0;padding:0}
html,body{width:1200px;height:3972px;overflow:hidden}
body{position:relative;background:var(--white);font-family:"Raleway",Arial,sans-serif;color:var(--text);font-size:13px}
.abs{position:absolute}
ul{list-style:none}

/* top bar */
.topbar{left:0;top:0;width:1200px;height:40px;border-bottom:1px solid var(--line);font-size:11px;font-weight:600;color:var(--ink)}
.topbar .left{left:56px;top:13px;display:flex;gap:26px}
.topbar .right{right:56px;top:8px;display:flex;gap:22px;align-items:center}
.topbar .item{display:flex;align-items:center;gap:6px}
.search{width:150px;height:24px;border:1px solid var(--line);border-radius:2px;padding:4px 8px;color:var(--muted);font-weight:500;display:flex;align-items:center;gap:6px}

/* nav */
.navbar{left:0;top:40px;width:1200px;height:100px}
.brand{left:56px;top:36px;display:flex;align-items:center;gap:10px;font-size:30px;font-weight:800;color:var(--ink);letter-spacing:1px}
.brand .mark{width:26px;height:26px;background:var(--ink)}
.menu{right:56px;top:36px;display:flex;font-size:12px;font-weight:700;color:var(--ink)}
.menu li{padding:8px 18px;border-left:1px solid var(--line)}
.menu li:first-child{border-left:0;border-bottom:2px solid var(--ink)}

/* hero */
.hero{left:56px;top:140px;width:1088px;height:520px;background:
  radial-gradient(ellipse 190px 300px at 470px 300px,rgba(235,235,235,.85),rgba(235,235,235,0) 70%),
  radial-gradient(ellipse 90px 70px at 470px 90px,rgba(60,45,40,.55),rgba(60,45,40,0) 80%),
  linear-gradient(100deg,#7d7e81 0%,#a7a8ab 30%,#b9babc 55%,#9fa0a3 80%,#86878a 100%);overflow:hidden}
.hero-title{left:60px;top:160px;color:var(--white);font-weight:800;letter-spacing:3px}
.hero-title .l1{font-size:26px}
.hero-title .l2{display:inline-block;margin:10px 0;padding:4px 14px;border:3px solid var(--white);font-size:50px;letter-spacing:4px}
.hero-title .l3{font-size:28px;letter-spacing:8px}
.callout{left:700px;width:330px;color:var(--white)}
.callout h3{font-size:15px;font-weight:700;letter-spacing:1px;margin-bottom:8px}
.callout p{font-size:11px;line-height:1.5;width:260px}
.callout .num{position:absolute;right:0;top:4px;width:34px;height:34px;border-radius:50%;border:2px solid var(--white);font-weight:700;display:flex;align-items:center;justify-content:center;font-size:14px}
.dots{left:494px;top:490px;display:flex;gap:8px}
.dots i{display:block;width:22px;height:3px;background:rgba(255,255,255,.5)}
.dots i:first-child{background:var(--white)}

/* sidebar */
.sidebar{left:56px;top:680px;width:356px;height:1560px;border:1px solid var(--line)}
.filter{border-bottom:1px solid var(--line);padding:18px 20px 14px 24px;position:relative}
.filter h4{font-size:15px;font-weight:800;color:var(--ink);letter-spacing:.5px;padding-bottom:12px;border-bottom:2px solid var(--ink);margin-bottom:10px}
.filter li{font-size:12px;color:var(--text);padding:5px 0 5px 28px;position:relative}
.filter li.on{background:var(--blue-soft);color:var(--ink);font-weight:600}
.filter li.on::before{content:"";position:absolute;left:9px;top:6px;width:6px;height:11px;border:solid var(--blue);border-width:0 3px 3px 0;transform:rotate(40deg)}
.filter li:not(.on)::before{content:"";position:absolute;left:6px;top:7px;width:11px;height:11px;border:1px solid #cfcfcf}
.filter .count{position:absolute;right:26px;color:var(--muted);font-size:11px}
.scroll{position:absolute;right:8px;top:70px;width:5px;border-radius:3px;background:#dcdcdc}
.scroll::after{content:"";display:block;height:40%;background:#9d9d9d;border-radius:3px}
.f-cat{height:560px}.f-cat li{padding-top:9px;padding-bottom:9px}
.f-len{height:390px}.f-waist{height:230px}.f-mat{height:378px;border-bottom:0}

/* feature block */
.feature{left:440px;top:680px;width:704px;height:568px}
.ph{position:absolute}
.ph-dress{left:0;top:0;width:360px;height:568px;background:
  radial-gradient(ellipse 120px 90px at 180px 110px,#c89a7e,rgba(200,154,126,0) 80%),
  linear-gradient(180deg,#e9e4de 0%,#d9b7a2 22%,#d36f6a 48%,#b9584f 65%,#e0a394 82%,#cfc6bd 100%)}
.ph-dress .label{position:absolute;left:0;top:256px;width:360px;height:56px;background:rgba(255,255,255,.7);font-size:24px;font-weight:700;color:var(--ink);display:flex;align-items:center;justify-content:center;letter-spacing:1px}
.ph-skirt{left:376px;top:0;width:328px;height:276px;background:
  radial-gradient(circle at 40% 55%,#f4f4f4 0 6px,transparent 7px) 0 0/34px 34px,
  linear-gradient(180deg,#f4f4f4 0%,#f4f4f4 18%,#1f1f1f 26%,#262626 78%,#e6d4c6 86%,#f1f1f1 100%)}
.ph-jeans{left:376px;top:292px;width:328px;height:276px;background:
  linear-gradient(90deg,#f0f0f0 0%,#f0f0f0 30%,#2c3140 38%,#3d4456 62%,#f0f0f0 70%,#f0f0f0 100%)}

.titlebar{left:440px;top:1288px;width:704px;height:42px;background:var(--dark);color:var(--white);font-size:15px;font-weight:700;padding:12px 20px;letter-spacing:.5px}
.controls{left:440px;top:1352px;width:704px;height:36px;font-size:11px;font-weight:600;color:var(--ink)}
.sort{position:absolute;left:0;top:0;width:210px;height:34px;border:1px solid var(--line);padding:10px 12px;color:var(--muted)}
.pager{position:absolute;left:288px;top:11px;display:flex;gap:10px}
.pager .cur{color:var(--ink)}.pager span{color:var(--muted)}
.seeall{position:absolute;right:0;top:0;height:34px;width:84px;background:var(--blue);color:var(--white);display:flex;align-items:center;justify-content:center}

.grid{left:440px;top:1420px;width:704px;display:grid;grid-template-columns:repeat(3,224px);column-gap:16px;row-gap:22px}
.card{height:240px;border-bottom:1px solid var(--line)}
.card .img{height:140px}
.card h5{font-size:11px;font-weight:700;color:var(--ink);line-height:1.35;margin:10px 6px 4px}
.card .by{font-size:9px;color:var(--muted);margin:0 6px}
.card .meta{display:flex;justify-content:space-between;margin:14px 6px 0;font-size:9px;font-weight:700;color:var(--ink)}
.card .meta span:last-child{color:var(--muted);font-weight:500}
.t1{background:linear-gradient(90deg,#d8cfc6 0%,#d8cfc6 35%,#c0504f 45%,#8a3d3b 60%,#d8cfc6 70%)}
.t2{background:linear-gradient(90deg,#f1efec 0%,#f1efec 35%,#c9b7a8 45%,#e2d6cc 60%,#f1efec 70%)}
.t3{background:linear-gradient(90deg,#c9a98a 0%,#c9a98a 35%,#2e2a29 45%,#4b4240 60%,#c9a98a 70%)}
.t4{background:linear-gradient(90deg,#e9e9ea 0%,#e9e9ea 35%,#6b7383 45%,#3f4656 60%,#e9e9ea 70%)}
.t5{background:linear-gradient(90deg,#f2f2f2 0%,#f2f2f2 35%,#3a3a3a 45%,#777 60%,#f2f2f2 70%)}
.t6{background:linear-gradient(90deg,#e8d9d2 0%,#e8d9d2 35%,#d98f8f 45%,#b8656a 60%,#e8d9d2 70%)}
.t7{background:linear-gradient(90deg,#cdb8a0 0%,#cdb8a0 35%,#a0524c 45%,#e1b7a4 60%,#cdb8a0 70%)}
.t8{background:linear-gradient(90deg,#dcd3c8 0%,#dcd3c8 35%,#c0604f 45%,#3c3434 60%,#dcd3c8 70%)}
.t9{background:linear-gradient(90deg,#d7c6b5 0%,#d7c6b5 35%,#b84d53 45%,#5b3d3a 60%,#d7c6b5 70%)}

/* earn points */
.earn{left:0;top:2290px;width:1200px;height:560px;background:var(--panel)}
.earn .head{position:absolute;left:0;top:48px;width:1200px;text-align:center}
.earn h2{font-size:20px;font-weight:800;color:var(--ink);letter-spacing:1px}
.earn .sub{font-size:12px;color:var(--muted);margin:6px 0 14px}
.btn-outline{display:inline-block;border:1px solid #bdbdbd;padding:8px 16px;font-size:10px;font-weight:700;color:var(--ink);background:var(--white)}
.lb{position:absolute;width:460px;height:80px;background:var(--white);border-top:4px solid var(--blue);display:flex;align-items:center;padding:0 20px;gap:18px}
.lb .rank{font-size:28px;font-weight:500;color:#b5b5b5;width:46px}
.lb .av{width:44px;height:44px;background:#d5d5d5;border-radius:2px}
.lb .name{flex:1;font-size:12px;font-weight:600;color:var(--ink)}
.lb .pts{font-size:24px;font-weight:800;color:var(--ink)}
.lb .pts small{font-size:11px;font-weight:600}
.arrow{position:absolute;top:280px}

/* progress */
.progress{left:0;top:2860px;width:1200px;height:300px;background:linear-gradient(90deg,#151516,#2b2b2e 50%,#17171a)}
.progress .stat{position:absolute;left:0;top:92px;width:1200px;text-align:center;color:var(--white);font-size:18px;font-weight:600}
.progress .stat b{font-weight:800}
.pbox{position:absolute;left:288px;top:146px;width:624px;height:106px;background:#3a3a3e;border-radius:14px;padding:24px 40px;color:var(--white)}
.pbox p{font-size:13px;font-weight:600;margin-bottom:14px}
.pbar{height:22px;background:#55565b;border-radius:3px;position:relative}
.pbar .fill{position:absolute;left:0;top:0;height:22px;width:30%;background:var(--blue);border-radius:3px}
.pbar .pct{position:absolute;left:150px;top:4px;font-size:11px;font-weight:700}

/* signup */
.signup{left:0;top:3170px;width:1200px;height:480px}
.signup h2{position:absolute;left:0;top:58px;width:1200px;text-align:center;font-size:18px;font-weight:800;color:var(--ink);letter-spacing:1px}
.signup .rule{position:absolute;left:580px;top:88px;width:40px;height:2px;background:var(--ink)}
.field{position:absolute;width:336px;height:42px;border:1px solid var(--line);padding:14px 14px;font-size:11px;color:var(--muted)}
.register{position:absolute;left:248px;top:296px;width:704px;height:52px;background:var(--blue);color:var(--white);font-weight:700;font-size:15px;display:flex;align-items:center;justify-content:center;letter-spacing:1px}
.signin{position:absolute;left:0;top:400px;width:1200px;text-align:center;font-size:12px;color:var(--muted)}
.signin b{color:var(--ink)}

/* footer */
.footer{left:0;top:3660px;width:1200px;height:280px;border-top:1px solid var(--line)}
.fcol{position:absolute;top:66px}
.fcol h6{font-size:13px;font-weight:800;color:var(--ink);margin-bottom:14px}
.fcol li,.fcol p{font-size:11px;color:var(--text);line-height:1.65}
.social{display:flex;gap:8px}
.social i{display:block;width:26px;height:26px;background:var(--blue)}
.copy{left:0;top:3940px;width:1200px;height:32px;background:var(--dark);color:#bbb;font-size:10px;padding:10px 56px}
</style>
</head>
<body>

<header>
  <div class="abs topbar">
    <div class="abs left">
      <span class="item"><svg width="11" height="11" viewBox="0 0 12 12"><circle cx="6" cy="4" r="3" fill="#1c1c1c"/><path d="M1 12c0-3 2.2-5 5-5s5 2 5 5z" fill="#1c1c1c"/></svg>LOGIN</span>
      <span class="item"><svg width="11" height="11" viewBox="0 0 12 12"><path d="M2 1h8v10H2z" fill="none" stroke="#1c1c1c" stroke-width="1.5"/></svg>SIGN UP</span>
    </div>
    <div class="abs right">
      <span class="item"><svg width="11" height="11" viewBox="0 0 12 12"><path d="M2 1l3 0 1 3-2 1c1 2 2 3 3 3l1-2 3 1v3c-6 0-10-4-10-9z" fill="#1c1c1c"/></svg>+1 555 014 2290</span>
      <span class="search"><svg width="11" height="11" viewBox="0 0 12 12"><circle cx="5" cy="5" r="3.5" fill="none" stroke="#8a8a8a" stroke-width="1.5"/><path d="M8 8l3 3" stroke="#8a8a8a" stroke-width="1.5"/></svg>Search...</span>
    </div>
  </div>
  <nav class="abs navbar">
    <div class="abs brand"><span class="mark"></span>VENDROW</div>
    <ul class="abs menu">
      <li>HOME</li><li>ABOUT US</li><li>BLOG</li><li>FORUMS</li><li>STANDINGS</li><li>CONTACT US</li>
    </ul>
  </nav>
</header>

<section class="abs hero" role="img" aria-label="Fashion photo of a model in a light jacket and grey trousers with feature callouts">
  <div class="abs hero-title">
    <div class="l1">CAN YOU FIND THE</div>
    <div class="l2">FEATURES</div>
    <div class="l3">IN THE IMAGE</div>
  </div>
  <svg class="abs" style="left:560px;top:90px" width="470" height="330" viewBox="0 0 470 330">
    <g stroke="#fff" stroke-dasharray="4 4" fill="none" stroke-width="1.2">
      <path d="M0 40 L120 20 H440"/><path d="M40 160 L140 140 H440"/><path d="M20 290 L120 270 H440"/>
    </g>
    <g fill="#fff"><circle cx="0" cy="40" r="4"/><circle cx="40" cy="160" r="4"/><circle cx="20" cy="290" r="4"/></g>
  </svg>
  <div class="abs callout" style="top:78px"><h3>TEXT MAIN REPLACE HERE</h3><p>Spot the neckline, sleeve and fabric details on this look to score your first points.</p><span class="num">1</span></div>
  <div class="abs callout" style="top:198px"><h3>TEXT MAIN REPLACE HERE</h3><p>Mark the jacket length and cut, then pick the right category from the list shown.</p><span class="num">2</span></div>
  <div class="abs callout" style="top:328px"><h3>TEXT MAIN REPLACE HERE</h3><p>Tag the trouser style and waistline correctly to climb higher on the weekly leaderboard.</p><span class="num">3</span></div>
  <div class="abs dots"><i></i><i></i><i></i></div>
</section>

<aside class="abs sidebar">
  <div class="filter f-cat">
    <h4>CATEGORIES</h4>
    <ul>
      <li class="on">Necklines<span class="count">(12)</span></li><li>Top<span class="count">(8)</span></li><li>Dress<span class="count">(6)</span></li><li>Jeans<span class="count">(4)</span></li><li>Pants<span class="count">(5)</span></li><li>Shorts<span class="count">(3)</span></li><li>Blouse<span class="count">(7)</span></li><li>Skirt<span class="count">(4)</span></li><li>Standard<span class="count">(2)</span></li><li>Crop Top<span class="count">(3)</span></li><li>Shirt<span class="count">(6)</span></li><li>Sweater<span class="count">(5)</span></li>
    </ul>
    <span class="scroll" style="height:440px"></span>
  </div>
  <div class="filter f-len">
    <h4>LENGTHS</h4>
    <ul>
      <li class="on">Boy Short</li><li>Regular Short</li><li>Bermuda</li><li>Pedal Pusher</li><li>Ankle</li><li>Full Length</li><li>Above waist</li><li>Waist &amp; Hipbone</li><li>Crotch &amp; Below</li><li>Micro &amp; Mini</li><li>Midi</li><li>Maxi</li>
    </ul>
    <span class="scroll" style="height:290px"></span>
  </div>
  <div class="filter f-waist">
    <h4>WAISTLINES</h4>
    <ul><li class="on">Empire</li><li>High-waist</li><li>Waist &amp; Hipbone</li><li>Drop-waist</li></ul>
    <span class="scroll" style="height:130px"></span>
  </div>
  <div class="filter f-mat">
    <h4>MATERIALS</h4>
    <ul><li class="on">Batiste</li><li>Lace</li><li>Eyelet</li><li>Fleece</li><li>Muslin</li><li>Chino</li><li>Veil</li><li>Poplin</li><li>Oxford</li></ul>
    <span class="scroll" style="height:250px"></span>
  </div>
</aside>

<section class="abs feature">
  <div class="ph ph-dress" role="img" aria-label="Model wearing a red floral summer dress"><div class="label">LOREM LIPSUM</div></div>
  <div class="ph ph-skirt" role="img" aria-label="Black mini skirt with white floral print"></div>
  <div class="ph ph-jeans" role="img" aria-label="Model in slim dark jeans and a black top"></div>
</section>

<div class="abs titlebar">TITLE HERE</div>
<div class="abs controls">
  <div class="sort">SORT BY ▾</div>
  <div class="pager"><span class="cur">PREVIOUS</span><span class="cur">1</span><span>2</span><span>3</span><span>4</span><span>5</span><span>...</span><span>10</span><span class="cur">NEXT</span></div>
  <div class="seeall">SEE ALL</div>
</div>

<section class="abs grid">
  <article class="card"><div class="img t1" role="img" aria-label="Model in a red printed top"></div><h5>LOREM LIPSUM IS A DUMMY TEXT OF INDUSTRY</h5><p class="by">Posted by team on style</p><div class="meta"><span>VIEW INFO</span><span>Jan 14, 2017</span></div></article>
  <article class="card"><div class="img t2" role="img" aria-label="Model in a light blouse"></div><h5>LOREM LIPSUM IS A DUMMY TEXT OF INDUSTRY</h5><p class="by">Posted by team on style</p><div class="meta"><span>VIEW INFO</span><span>Jan 16, 2017</span></div></article>
  <article class="card"><div class="img t3" role="img" aria-label="Model in a dark jacket"></div><h5>LOREM LIPSUM IS A DUMMY TEXT OF INDUSTRY</h5><p class="by">Posted by team on style</p><div class="meta"><span>VIEW INFO</span><span>Jan 18, 2017</span></div></article>
  <article class="card"><div class="img t4" role="img" aria-label="Model in a denim outfit"></div><h5>LOREM LIPSUM IS A DUMMY TEXT OF INDUSTRY</h5><p class="by">Posted by team on style</p><div class="meta"><span>VIEW INFO</span><span>Jan 20, 2017</span></div></article>
  <article class="card"><div class="img t5" role="img" aria-label="Model in a black coat"></div><h5>LOREM LIPSUM IS A DUMMY TEXT OF INDUSTRY</h5><p class="by">Posted by team on style</p><div class="meta"><span>VIEW INFO</span><span>Jan 22, 2017</span></div></article>
  <article class="card"><div class="img t6" role="img" aria-label="Model in a pink knit sweater"></div><h5>LOREM LIPSUM IS A DUMMY TEXT OF INDUSTRY</h5><p class="by">Posted by team on style</p><div class="meta"><span>VIEW INFO</span><span>Jan 24, 2017</span></div></article>
  <article class="card"><div class="img t7" role="img" aria-label="Model in a patterned dress"></div><h5>LOREM LIPSUM IS A DUMMY TEXT OF INDUSTRY</h5><p class="by">Posted by team on style</p><div class="meta"><span>VIEW INFO</span><span>Jan 26, 2017</span></div></article>
  <article class="card"><div class="img t8" role="img" aria-label="Model in a red top and black skirt"></div><h5>LOREM LIPSUM IS A DUMMY TEXT OF INDUSTRY</h5><p class="by">Posted by team on style</p><div class="meta"><span>VIEW INFO</span><span>Jan 28, 2017</span></div></article>
  <article class="card"><div class="img t9" role="img" aria-label="Model in a crimson crop top"></div><h5>LOREM LIPSUM IS A DUMMY TEXT OF INDUSTRY</h5><p class="by">Posted by team on style</p><div class="meta"><span>VIEW INFO</span><span>Jan 30, 2017</span></div></article>
</section>

<section class="abs earn">
  <div class="head">
    <h2>EARN POINTS</h2>
    <p class="sub">and see where you stand</p>
    <span class="btn-outline">SEE LEADERBOARD</span>
  </div>
  <svg class="arrow" style="left:56px" width="14" height="20" viewBox="0 0 14 20"><path d="M11 2L3 10l8 8" fill="none" stroke="#1c1c1c" stroke-width="3"/></svg>
  <svg class="arrow" style="left:1130px" width="14" height="20" viewBox="0 0 14 20"><path d="M3 2l8 8-8 8" fill="none" stroke="#1c1c1c" stroke-width="3"/></svg>
  <div class="lb" style="left:128px;top:222px"><span class="rank">#1</span><span class="av"></span><span class="name">DUMMY USERNAME</span><span class="pts">100 <small>pts</small></span></div>
  <div class="lb" style="left:612px;top:222px"><span class="rank">#2</span><span class="av"></span><span class="name">DUMMY USERNAME</span><span class="pts">99 <small>pts</small></span></div>
  <div class="lb" style="left:128px;top:334px"><span class="rank">#3</span><span class="av"></span><span class="name">DUMMY USERNAME</span><span class="pts">98 <small>pts</small></span></div>
  <div class="lb" style="left:612px;top:334px"><span class="rank">#4</span><span class="av"></span><span class="name">DUMMY USERNAME</span><span class="pts">97 <small>pts</small></span></div>
</section>

<section class="abs progress">
  <p class="stat"><b>300,000</b> images processed by <b>1,000</b> participants</p>
  <div class="pbox">
    <p>x% of 1,000,000 goal a month left</p>
    <div class="pbar"><span class="fill"></span><span class="pct">30%</span></div>
  </div>
</section>

<section class="abs signup">
  <h2>SIGN-UP</h2><span class="rule"></span>
  <div class="field" style="left:248px;top:118px">First name</div>
  <div class="field" style="left:616px;top:118px">Last name</div>
  <div class="field" style="left:248px;top:180px">Phone</div>
  <div class="field" style="left:616px;top:180px">Email</div>
  <div class="field" style="left:248px;top:240px">Password</div>
  <div class="field" style="left:616px;top:240px">Confirm Password</div>
  <div class="register">REGISTER</div>
  <p class="signin">Already have an account? <b>Sign in here</b></p>
</section>

<footer class="abs footer">
  <div class="fcol" style="left:56px"><h6>Quick links</h6><ul><li>Home</li><li>About us</li><li>Blog</li><li>Forums</li><li>Standings</li><li>Contact Us</li></ul></div>
  <div class="fcol" style="left:316px"><h6>About Points</h6><ul><li>Terms &amp; Conditions</li><li>Eligibility</li><li>Winners &amp; Prizes</li><li>Privacy Policy</li><li>Judging</li><li>Disclaimer</li></ul></div>
  <div class="fcol" style="left:628px"><h6>Contact Us</h6><p>Phone: 555-014-7731</p><p>Email: hello@vendrow.example</p><p>Studio 4, 210 Harbour Lane,<br>Westfield, NY 10023</p></div>
  <div class="fcol" style="left:980px"><h6>Social Media</h6><div class="social"><i></i><i></i><i></i><i></i></div></div>
</footer>
<div class="abs copy">Copyright 2016, vendrow. All Rights Reserved</div>

</body>
</html>
```